St Louis Electrician Needing a Business Card Design!!

We are a St Louis based electrical contracting firm that needs help designing a business card. We have a logo and I have another image that I would like to incorporate. Open to ideas..Thanks!!

Industry/Entity Type

Business

Requirements
Must have
• there are two downloads...one is the logo and the other is what i was wanting coming off the logo...the light rays. Like the logo with the blue background...Was thinking the whole card would be that color blue.
Should not have
• No lightning bolts

```html
<!DOCTYPE html>
<html lang="en">
<head>
<meta charset="utf-8">
<title>Voltaris Inc. – Business Card</title>
<link href="https://fonts.googleapis.com/css2?family=Arimo:wght@400;700&display=swap" rel="stylesheet">
<style>
  :root {
    --brand-blue: #1257a6;
    --text-grey: #a3a3a3;
    --band-grey: #a6a8aa;
    --paper: #ffffff;
  }
  html, body {
    margin: 0;
    padding: 0;
    width: 1200px;
    height: 699px;
    overflow: hidden;
    background: var(--paper);
  }
  .card {
    position: relative;
    width: 1200px;
    height: 699px;
    background: var(--paper);
    font-family: "Arimo", Arial, sans-serif;
    overflow: hidden;
  }
  .brand {
    position: absolute;
    left: 56px;
    top: 98px;
    display: flex;
    align-items: center;
    gap: 14px;
  }
  .brand-dot {
    width: 22px;
    height: 22px;
    border-radius: 50%;
    background: var(--brand-blue);
  }
  .brand-name {
    margin: 0;
    font-size: 50px;
    font-weight: 400;
    color: var(--brand-blue);
    letter-spacing: -0.5px;
  }
  .address {
    position: absolute;
    left: 55px;
    top: 272px;
    margin: 0;
    font-style: normal;
    font-weight: 700;
    font-size: 22px;
    line-height: 29px;
    color: var(--text-grey);
  }
  .identity {
    position: absolute;
    right: 91px;
    top: 334px;
    text-align: right;
  }
  .person-name {
    margin: 0;
    font-size: 37px;
    font-weight: 700;
    color: var(--brand-blue);
    line-height: 1.1;
  }
  .person-title {
    margin: 6px 0 0;
    font-size: 22px;
    font-weight: 400;
    color: var(--text-grey);
  }
  .contacts {
    position: absolute;
    left: 54px;
    top: 402px;
    margin: 0;
    padding: 0;
    list-style: none;
  }
  .contact-item {
    display: flex;
    align-items: center;
    height: 30px;
    margin-bottom: 9px;
    font-size: 17px;
    color: var(--text-grey);
  }
  .contact-icon {
    width: 30px;
    height: 30px;
    margin-right: 16px;
    fill: var(--brand-blue);
    stroke: var(--brand-blue);
  }
  .footer-bands {
    position: absolute;
    left: 0;
    bottom: 0;
    width: 1200px;
    height: 44px;
  }
  .band-grey { fill: var(--band-grey); }
  .band-blue { fill: var(--brand-blue); }
</style>
</head>
<body>
<main class="card">
  <div class="brand">
    <span class="brand-dot"></span>
    <h1 class="brand-name">Voltaris Inc.</h1>
  </div>

  <address class="address">1840 Harlow Ave<br>St. Louis, MO 63139</address>

  <section class="identity">
    <h2 class="person-name">Daniel Reeves</h2>
    <p class="person-title">Marketing Manager</p>
  </section>

  <ul class="contacts">
    <li class="contact-item">
      <svg class="contact-icon" viewBox="0 0 30 30" aria-hidden="true">
        <path stroke="none" d="M6 3c1-1 2.5-1 3.3 0l3 4c.7 1 .6 2.2-.2 3l-1.7 1.6c1.3 3 3.8 5.6 6.9 7l1.7-1.7c.8-.8 2-.9 3-.2l4 3c1 .8 1 2.3 0 3.3l-2 2c-1.6 1.6-4.2 2-6.3.9C11.5 23.5 6.5 18.5 3.1 12.3 2 10.2 2.4 7.6 4 6z"/>
      </svg>
      <span>314-xxx-xxxx</span>
    </li>
    <li class="contact-item">
      <svg class="contact-icon" viewBox="0 0 30 30" aria-hidden="true">
        <rect stroke="none" x="1" y="13" width="6" height="13"/>
        <rect stroke="none" x="8.5" y="10" width="6" height="16"/>
        <rect stroke="none" x="16" y="7" width="6" height="19"/>
        <rect stroke="none" x="23.5" y="4" width="6" height="22"/>
      </svg>
      <span>314-xxx-xxxx</span>
    </li>
    <li class="contact-item">
      <svg class="contact-icon" viewBox="0 0 30 30" aria-hidden="true">
        <rect x="2" y="7" width="26" height="17" fill="none" stroke-width="2"/>
        <path d="M2 7l13 10 13-10M2 24l10-9M28 24l-10-9" fill="none" stroke-width="2"/>
      </svg>
      <span>daniel.reeves@voltarisco.com</span>
    </li>
    <li class="contact-item">
      <svg class="contact-icon" viewBox="0 0 30 30" aria-hidden="true">
        <circle cx="15" cy="15" r="12" fill="none" stroke-width="2.2"/>
        <ellipse cx="15" cy="15" rx="5.5" ry="12" fill="none" stroke-width="2"/>
        <path d="M3 15h24M5 9h20M5 21h20" fill="none" stroke-width="2"/>
      </svg>
      <span>www.voltariselectricco.com</span>
    </li>
  </ul>

  <svg class="footer-bands" viewBox="0 0 1200 44" aria-hidden="true">
    <polygon class="band-grey" points="0,22 762,22 744,44 0,44"/>
    <polygon class="band-blue" points="795,0 1200,0 1200,44 759,44"/>
  </svg>
</main>
</body>
</html>
```